Brightwire Hollow Business cards

one side I would like my logo (uploaded) and the other side I want my details. I'm an electrician in sydney. The logo side I'm happy with just a white background and our logo in the middle.

Details for other side
24/7 Sydney Electrician
Marcus Pell
0431 587 219
marcus@brightwirehollow.com.au
brightwirehollow.com.au
icons for facebook, instagram, linked in

Industry/Entity Type

electrician

Contact Information for Business Card

company info

```html
<!DOCTYPE html>
<html lang="en">
<head>
<meta charset="utf-8">
<title>Brightwire Hollow — Business Cards</title>
<link href="https://fonts.googleapis.com/css2?family=Roboto:wght@400;700&display=swap" rel="stylesheet">
<style>
  :root {
    --backdrop: #c9c9cb;
    --paper: #f2f2f2;
    --ink: #111111;
    --night: #000000;
    --signal-red: #e31e24;
    --light-text: #ffffff;
  }
  * { box-sizing: border-box; margin: 0; padding: 0; }
  html, body {
    width: 1200px; height: 1131px; overflow: hidden;
    background: var(--backdrop);
    font-family: "Roboto", Arial, sans-serif;
  }
  .stage {
    position: relative; width: 1200px; height: 1131px;
    display: flex; flex-direction: column; align-items: center; justify-content: center; gap: 56px;
  }
  .card {
    position: relative; width: 840px; height: 480px; overflow: hidden;
    background: var(--paper);
    box-shadow: 0 10px 30px rgba(0,0,0,0.18);
  }
  /* Details side */
  .details-card { display: flex; }
  .details-brand-half { position: relative; width: 50%; height: 100%; }
  .details-contact-half {
    position: relative; width: 50%; height: 100%;
    background: var(--night); color: var(--light-text);
  }
  .wordmark {
    font-weight: 700; color: var(--signal-red);
    text-transform: uppercase; letter-spacing: 1px; line-height: 1;
  }
  .details-brand-half .wordmark {
    position: absolute; left: 44px; top: 62px; font-size: 40px; width: 340px;
  }
  .service-line { position: absolute; left: 44px; bottom: 44px; }
  .service-hours { font-size: 34px; font-weight: 700; color: var(--signal-red); line-height: 1; }
  .service-area { font-size: 19px; color: var(--ink); margin-top: 4px; }
  .social-row {
    position: absolute; right: 40px; bottom: 150px; display: flex; gap: 26px;
  }
  .social-dot { width: 34px; height: 34px; border-radius: 50%; background: var(--signal-red); }
  .owner { position: absolute; right: 44px; top: 44px; text-align: right; }
  .owner-name { font-size: 40px; font-weight: 700; line-height: 1.05; }
  .owner-phone {
    font-size: 24px; margin-top: 8px; display: flex; align-items: center; justify-content: flex-end; gap: 10px;
    letter-spacing: 1px;
  }
  .contact-list {
    position: absolute; right: 40px; bottom: 46px; list-style: none;
    display: flex; flex-direction: column; gap: 12px;
  }
  .contact-item { display: flex; align-items: center; gap: 12px; font-size: 21px; }
  .contact-item svg, .owner-phone svg { flex: none; }
  /* Logo side */
  .logo-card { display: flex; align-items: center; justify-content: center; }
  .logo-card .wordmark { font-size: 62px; }
</style>
</head>
<body>
<main class="stage">
  <section class="card details-card" aria-label="Business card, details side">
    <div class="details-brand-half">
      <p class="wordmark">Brightwire Hollow</p>
      <div class="social-row" aria-label="Social links">
        <span class="social-dot"></span>
        <span class="social-dot"></span>
        <span class="social-dot"></span>
      </div>
      <div class="service-line">
        <p class="service-hours">24/7</p>
        <p class="service-area">Sydney Electricians</p>
      </div>
    </div>
    <div class="details-contact-half">
      <div class="owner">
        <p class="owner-name">Marcus Pell</p>
        <p class="owner-phone">
          <svg width="18" height="18" viewBox="0 0 24 24" aria-hidden="true"><path fill="#e31e24" d="M6.6 10.8a15 15 0 0 0 6.6 6.6l2.2-2.2c.3-.3.7-.4 1-.2 1.1.4 2.3.6 3.6.6.6 0 1 .4 1 1V20c0 .6-.4 1-1 1A17 17 0 0 1 3 4c0-.6.4-1 1-1h3.5c.6 0 1 .4 1 1 0 1.3.2 2.5.6 3.6.1.3 0 .7-.2 1z"/></svg>
          0431 587 219
        </p>
      </div>
      <ul class="contact-list">
        <li class="contact-item">
          <svg width="22" height="16" viewBox="0 0 22 16" aria-hidden="true"><rect width="22" height="16" rx="1" fill="#e31e24"/><path d="M1 1l10 8 10-8" fill="none" stroke="#000" stroke-width="1.6"/></svg>
          marcus@brightwirehollow.com.au
        </li>
        <li class="contact-item">
          <svg width="20" height="20" viewBox="0 0 20 20" aria-hidden="true"><circle cx="10" cy="10" r="9" fill="#e31e24"/><path d="M1 10h18M10 1c-4 4-4 14 0 18M10 1c4 4 4 14 0 18" fill="none" stroke="#000" stroke-width="1.3"/></svg>
          brightwirehollow.com.au
        </li>
      </ul>
    </div>
  </section>

  <section class="card logo-card" aria-label="Business card, logo side">
    <p class="wordmark">Brightwire Hollow</p>
  </section>
</main>
</body>
</html>
```